HVAC Door Hanger- 4.25 inches by 11 inches

Hello We are using the Brightwell door hanger as an inspiration for our new door hanger. The company name is Harborline Home Services. Logo files attached. The Slogan needs to be added on the front with the Logo "Southern California’s Trusted Name in Home Services". Instead of the X protection plan, the name will be Full Shield by Harborline or Harborline Climate Keeper- The slogan for this package will be "Peace of Mind, For Every Season

```html
<!DOCTYPE html>
<html lang="en">
<head>
<meta charset="utf-8">
<title>Harborline Home Services – Door Hanger</title>
<link href="https://fonts.googleapis.com/css2?family=Oswald:wght@400;500&family=Roboto:wght@400;500;700;900&display=swap" rel="stylesheet">
<style>
  :root {
    --brand-blue: #1f82d6;
    --brand-orange: #fb8c00;
    --alert-red: #e8141b;
    --paper: #ffffff;
    --ink: #111111;
    --hole-edge: #c9c9c9;
  }
  * { box-sizing: border-box; margin: 0; padding: 0; }
  html, body { width: 1200px; height: 1000px; overflow: hidden; background: var(--paper); }
  body { position: relative; font-family: "Roboto", Arial, sans-serif; }

  .hanger { position: absolute; left: 50px; width: 1100px; height: 425px; box-shadow: 0 2px 4px rgba(0,0,0,.18); }
  .hanger--front { top: 37px; }
  .hanger--back { top: 537px; }
  .hanger__frame { position: absolute; inset: 0; width: 1100px; height: 425px; }
  .hanger > *:not(.hanger__frame) { position: absolute; }

  .fine-print { right: 38px; top: 383px; font-size: 8px; font-weight: 500; color: var(--ink); }

  /* front */
  .front-slogan { left: 49px; top: 44px; color: var(--paper); font-size: 30px; font-weight: 500; line-height: 36px; text-transform: uppercase; }
  .front-brand { left: 49px; top: 196px; color: var(--brand-blue); font-size: 55px; font-weight: 900; letter-spacing: 0.5px; white-space: nowrap; }

  /* back */
  .season-headline { left: 49px; top: 44px; color: var(--paper); font-size: 37px; font-weight: 900; white-space: nowrap; }
  .schedule-cta { left: 780px; top: 47px; width: 270px; text-align: right; color: var(--brand-blue); font-size: 15px; font-weight: 500; }
  .schedule-phone { left: 760px; top: 63px; width: 290px; text-align: right; color: var(--alert-red); font-size: 38px; font-weight: 700; }

  .plan-title { left: 49px; top: 142px; color: var(--brand-blue); font-size: 29px; font-weight: 700; white-space: nowrap; }
  .plan-price { left: 49.5px; top: 199.5px; width: 475px; height: 60px; background: var(--brand-orange); color: var(--paper); text-align: center; padding-top: 6px; }
  .plan-price__headline { font-size: 22px; font-weight: 700; line-height: 26px; }
  .plan-price__detail { font-size: 17px; font-weight: 500; line-height: 22px; }
  .plan-price__new { color: var(--ink); font-weight: 700; font-size: 20px; }

  .plan-includes { left: 49.5px; top: 280px; width: 475px; height: 88px; border: 1px dashed var(--brand-blue); border-radius: 6px; }
  .plan-includes__list { position: absolute; list-style: none; top: 18px; font-family: "Oswald", "Arial Narrow", sans-serif; font-size: 14px; line-height: 20px; color: var(--ink); }
  .plan-includes__list--left { left: 13px; }
  .plan-includes__list--right { left: 259px; }
  .plan-includes__list li::before { content: "• "; }
  .pill { left: 206px; width: 162px; height: 20px; border-radius: 10px; background: var(--brand-blue); color: var(--paper); font-size: 16px; font-weight: 500; text-align: center; line-height: 20px; }
  .pill--top { top: 269px; }
  .pill--bottom { top: 359px; }

  .offers { left: 549px; top: 130.5px; width: 350px; height: 243.5px; background: var(--brand-blue); border: 2px solid var(--brand-blue); color: var(--paper); }
  .offers__banner { position: absolute; left: 5px; top: 4px; width: 336px; height: 24px; background: var(--brand-orange); text-align: center; font-size: 19px; font-weight: 500; letter-spacing: 2px; line-height: 24px; }
  .offers__special { position: absolute; left: 13px; top: 60px; font-size: 28px; font-weight: 400; line-height: 30px; letter-spacing: .5px; }
  .offers__only { position: absolute; left: 13px; top: 123px; font-size: 16px; font-weight: 500; }
  .offers__amount { position: absolute; left: 29px; top: 118px; font-size: 72px; font-weight: 700; line-height: 80px; }
  .offers__amount sup { font-size: 46px; vertical-align: 8px; }
  .offers__reg { position: absolute; left: 13px; top: 186px; font-size: 22px; letter-spacing: 2px; }
  .offers__list { position: absolute; left: 160px; top: 44px; width: 182px; list-style: none; font-family: "Oswald", "Arial Narrow", sans-serif; font-size: 14px; line-height: 20px; text-align: center; }
  .offers__list li + li { margin-top: 10px; padding-top: 10px; border-top: 1.5px solid var(--brand-orange); }
  .offers__list li + li { border-image: linear-gradient(90deg, transparent 15%, var(--brand-orange) 15%, var(--brand-orange) 85%, transparent 85%) 1; }

  .rebate { left: 899px; top: 300px; width: 150px; height: 74px; background: var(--brand-orange); color: var(--paper); padding: 4px 0 0 9px; font-family: "Oswald", "Arial Narrow", sans-serif; font-size: 17px; font-weight: 500; line-height: 21px; }
</style>
</head>
<body>

<section class="hanger hanger--front">
  <svg class="hanger__frame" viewBox="0 0 1466 566" aria-hidden="true">
    <rect width="1466" height="566" fill="var(--brand-blue)"/>
    <polygon points="0,0 1100,0 1070,33 0,33" fill="var(--brand-orange)"/>
    <polygon points="1100,0 1130,0 1100,33 1433,33 1433,533 33,533 33,183 920,183 1070,33" fill="var(--paper)"/>
    <circle cx="1319" cy="282" r="80" fill="var(--paper)" stroke="var(--hole-edge)" stroke-width="3"/>
    <line x1="1393" y1="246" x2="1466" y2="208" stroke="var(--hole-edge)" stroke-width="2"/>
  </svg>
  <p class="front-slogan">Southern California’s Trusted Name<br>in Home Services</p>
  <p class="front-brand">HARBORLINE HOME SERVICES</p>
  <p class="fine-print">*Offers cannot be combined. Offers expire 12/8/25 &nbsp;I&nbsp; HVAC #1234567</p>
</section>

<section class="hanger hanger--back">
  <svg class="hanger__frame" viewBox="0 0 1466 566" aria-hidden="true">
    <rect width="1466" height="566" fill="var(--brand-blue)"/>
    <polygon points="0,0 1100,0 1070,33 0,33" fill="var(--brand-orange)"/>
    <polygon points="1100,0 1130,0 1100,33 1433,33 1433,533 33,533 33,132 971,132 1070,33" fill="var(--paper)"/>
    <circle cx="1319" cy="282" r="80" fill="var(--paper)" stroke="var(--hole-edge)" stroke-width="3"/>
    <line x1="1393" y1="319" x2="1466" y2="357" stroke="var(--hole-edge)" stroke-width="2"/>
  </svg>

  <h1 class="season-headline">PEACE OF MIND, FOR EVERY SEASON</h1>
  <p class="schedule-cta">Schedule your service today &amp; save!</p>
  <p class="schedule-phone">(000) 123-4567</p>

  <h2 class="plan-title">FULL SHIELD BY HARBORLINE</h2>
  <div class="plan-price">
    <p class="plan-price__headline">MONTHLY SERVICE REDUCED</p>
    <p class="plan-price__detail">From $29.99/Month To <span class="plan-price__new">$19.99</span>/Month</p>
  </div>

  <div class="plan-includes">
    <ul class="plan-includes__list plan-includes__list--left">
      <li>ONE HEATING TUNE-UP PER YEAR</li>
      <li>ONE A/C TUNE-UP PER YEAR</li>
      <li>10% OFF IN-DOOR AIR QUALITY PRODUCTS</li>
    </ul>
    <ul class="plan-includes__list plan-includes__list--right">
      <li>ONE WATER HEATER FLUSH PER YEAR</li>
      <li>PRIORITY INSTALLATION</li>
      <li>TRANSFERRABLE PLAN</li>
    </ul>
  </div>
  <p class="pill pill--top">INCLUDES</p>
  <p class="pill pill--bottom">AND MUCH MORE</p>

  <div class="offers">
    <p class="offers__banner">LIMITED TIME OFFERS!</p>
    <p class="offers__special">HALF OFF<br>SPECIAL!</p>
    <p class="offers__only">ONLY</p>
    <p class="offers__amount"><sup>$</sup>88</p>
    <p class="offers__reg">Reg. $176</p>
    <ul class="offers__list">
      <li>A/C SYSTEM<br>SAFETY INSPECTION + TUNE-UP</li>
      <li>STANDARD WATER HEATER FLUSH</li>
      <li>WHOLE HOME WATER<br>SAFETY INSPECTION</li>
      <li>ACCESSIBLE DRAIN CLEANING</li>
    </ul>
  </div>

  <p class="rebate">GET UP TO $10,000<br>IN STATE &amp; FEDERAL<br>REBATES!!!</p>

  <p class="fine-print">*Offers cannot be combined. Offers expire 12/8/25 &nbsp;I&nbsp; HVAC #1234567</p>
</section>

</body>
</html>
```